The tooth corner of brimwell web page

website for dental office
Already have domain, mostly information only with address, telephone and google map and hours of operation on top. mobile friendly. SEO a most.

Target Market(s)

Local families

Industry/Entity Type

Dental Clinic

Number of Pages Required

1 page

Font styles to use
Serif

Colors

Designer to choose colors to be used in the design.

Requirements
Must have
• SEO
• Information to find the location
• mobile friendly
• dr's. biography
• services offered
• contect to social media (google, facebook, and instagram)
• Se habla espaƱol
• All insurance accepted
• request an appointment form to notify us

```html
<!DOCTYPE html>
<html lang="en">
<head>
<meta charset="utf-8">
<title>The Tooth Corner of Brimwell</title>
<link rel="stylesheet" href="https://fonts.googleapis.com/css2?family=Oswald:wght@400;500&family=Poppins:ital,wght@0,400;0,500;0,600;1,400&display=swap">
<style>
:root{
  --blue:#0d55a5;
  --blue-deep:#0b3f82;
  --sky:#1da1d8;
  --green:#8dc63f;
  --ink:#333;
  --muted:#666;
  --light:#f7f7f8;
  --line:#dcdcdc;
  --dark:#2d2d2d;
  --topbar:#3a3a3a;
}
*{box-sizing:border-box;margin:0;padding:0}
html,body{width:1200px;height:3774px;overflow:hidden;background:#fff}
body{font-family:'Poppins',sans-serif;color:var(--ink)}
.page{position:relative;width:1200px;height:3774px;overflow:hidden}
.abs{position:absolute}

/* header */
.topbar{left:520px;top:0;width:680px;height:42px;background:var(--topbar);color:#fff;font-size:11px}
.topbar .socials{position:absolute;left:12px;top:12px;display:flex;gap:8px}
.topbar .socials span{width:16px;height:16px;border-radius:50%;background:#fff;display:block}
.topbar .item{position:absolute;top:4px;display:flex;gap:8px;align-items:center;line-height:1.25}
.topbar .item b{font-size:15px;font-weight:600;display:block}
.topbar .item small{font-size:10px;display:block}
.new-patients{position:absolute;right:0;top:0;width:250px;height:46px;background:var(--blue);color:#fff;text-align:center;font-size:14px;font-weight:600;padding-top:6px;line-height:1.2}
.new-patients small{display:block;font-size:10px;font-weight:400}
.header{left:0;top:0;width:1200px;height:122px;background:rgba(255,255,255,.92)}
.brand{position:absolute;left:150px;top:18px;display:flex;align-items:center;gap:10px}
.brand-dot{width:44px;height:44px;border-radius:50%;background:var(--blue)}
.brand-name{font-size:15px;font-weight:600;color:var(--blue);line-height:1.2;width:120px}
.nav{position:absolute;left:462px;top:78px;display:flex;gap:38px;font-size:13px;font-weight:600;color:var(--blue-deep);letter-spacing:.5px}
.nav .active{border-bottom:2px solid var(--blue);padding-bottom:4px}

/* hero */
.hero{left:0;top:0;width:1200px;height:810px;background:linear-gradient(100deg,#e9e9ea 0%,#d7d3d2 35%,#c9a99a 60%,#b88f7d 80%,#d8d2cf 100%)}
.hero-title{left:113px;top:288px;font-family:'Oswald',sans-serif;font-size:36px;color:#111;letter-spacing:.5px}
.hero-sub{left:113px;top:338px;width:430px;font-size:15px;font-weight:500;color:#222;line-height:1.65}
.btn{display:inline-block;background:var(--green);color:#fff;font-weight:600;font-size:11px;border-radius:20px;text-align:center;letter-spacing:.3px}
.hero-btn{left:113px;top:403px;width:116px;height:38px;line-height:38px}
.hero-wave{left:0;top:560px}

/* section headings */
.heading{width:1200px;left:0;text-align:center;font-size:34px;font-weight:500;color:var(--blue);letter-spacing:.5px}
.rule{left:545px;width:110px;height:1px;background:var(--line)}

.services-intro{left:240px;top:905px;width:720px;text-align:center;font-size:12px;line-height:2;color:var(--muted)}
.service{width:250px;text-align:center}
.service .ring{width:214px;height:214px;margin:0 auto;border-radius:50%;background:#f1f1f1;display:flex;align-items:center;justify-content:center}
.service .ring div{width:180px;height:180px;border-radius:50%;background:#fff;box-shadow:0 2px 8px rgba(0,0,0,.08);display:flex;align-items:center;justify-content:center}
.service h3{margin-top:22px;font-size:17px;font-weight:600;color:var(--blue-deep)}
.service p{margin:6px auto 0;width:170px;font-size:11px;line-height:1.6;color:var(--ink)}
.service .btn{margin-top:20px;width:106px;height:35px;line-height:35px;font-size:10px}

/* about */
.doctor-photo{left:113px;top:1585px;width:387px;height:465px;background:linear-gradient(180deg,#fff 0%,#f1ece8 45%,#dcd9d6 100%)}
.doctor-name{left:113px;top:2000px;width:387px;height:50px;background:var(--sky);color:#fff;font-size:17px;font-weight:600;text-align:center;line-height:50px}
.about-text{left:558px;top:1642px;width:545px;text-align:center;font-size:12.5px;line-height:2.1;color:var(--ink)}
.circle-row{display:flex;gap:26px}
.circle-row span{width:50px;height:50px;border-radius:50%;background:#f0f0f0;display:block}

/* testimonials */
.testimonials{left:0;top:2139px;width:1200px;height:700px;background:var(--light)}
.avatar{left:543px;top:2333px;width:114px;height:114px;border-radius:50%;background:linear-gradient(180deg,#dfe6ee,#b9c9d9);border:4px solid #fff}
.stars{left:0;top:2470px;width:1200px;text-align:center;font-size:18px;color:#e8b30e;letter-spacing:2px}
.quote{left:220px;top:2510px;width:760px;text-align:center;font-size:13px;font-style:italic;line-height:2.3;color:var(--ink)}
.patient{left:0;top:2655px;width:1200px;text-align:center;font-size:11px;font-weight:600;color:var(--green)}
.patient small{display:block;font-weight:400;color:#999;font-size:10px}

/* contact */
.contact-band{left:0;top:2580px}
.subscribe{left:113px;top:2863px;display:flex;height:50px}
.subscribe .field{width:340px;background:var(--blue-deep);color:#fff;font-size:13px;padding:15px 14px}
.subscribe .btn{width:128px;border-radius:0;line-height:50px;font-size:15px}
.contact-title{left:113px;top:2955px;font-size:33px;color:#fff;font-weight:500}
.contact-line{left:113px;color:#fff;font-size:14px;display:flex;gap:12px;align-items:flex-start;line-height:1.5}
.contact-line b{font-size:19px;font-weight:500;margin-left:8px}
.appointment{left:584px;top:2949px;width:503px;height:397px;background:var(--blue-deep);padding:24px 22px}
.appointment h2{font-size:31px;color:#fff;font-weight:500;line-height:1}
.appointment p{font-size:11px;color:#fff;margin-top:4px}
.form{position:absolute;left:22px;top:90px;width:459px}
.form .row{display:flex;gap:12px;margin-bottom:13px}
.form .input{flex:1;height:38px;background:#fff;font-size:12px;color:#333;padding:11px 10px}
.form .area{height:112px;background:#fff;font-size:12px;padding:11px 10px;margin-bottom:24px}
.form .submit{height:44px;background:var(--green);color:#fff;text-align:center;line-height:44px;font-size:16px;font-weight:500}
.map{left:0;top:3271px;width:1200px;height:314px;background:linear-gradient(135deg,#e8e6e2,#d9d7d3 50%,#e4e2de)}
.footer{left:0;top:3585px;width:1200px;height:189px;background:var(--dark)}
.footer .circle-row{position:absolute;left:498px;top:50px;gap:30px}
.footer .circle-row span{background:var(--green);border:3px solid #fff}
.copyright{position:absolute;left:0;top:125px;width:1200px;text-align:center;color:#ddd;font-size:11px}
.map-card{z-index:1}
</style>
</head>
<body>
<div class="page">

  <div class="abs hero" role="img" aria-label="Photo of a smiling patient during a dental check-up"></div>
  <svg class="abs hero-wave" width="1200" height="260" viewBox="0 0 1200 260"><path d="M0 80 C180 200 330 260 520 220 C700 180 760 60 930 40 C1040 28 1120 60 1200 70 L1200 260 L0 260 Z" fill="#fff"/></svg>

  <header>
    <div class="abs header">
      <div class="brand"><span class="brand-dot"></span><span class="brand-name">The Tooth Corner of Brimwell</span></div>
      <nav class="nav"><span class="active">ABOUT US</span><span>DENTISTS</span><span>SERVICES</span><span>CASE HISTORIES</span><span>INFORMATION</span><span>CONTACT</span></nav>
    </div>
    <div class="abs topbar">
      <div class="socials"><span></span><span></span><span></span></div>
      <div class="item" style="left:110px">
        <svg width="16" height="16" viewBox="0 0 24 24"><path d="M6.6 10.8a15 15 0 0 0 6.6 6.6l2.2-2.2a1 1 0 0 1 1-.25 11.4 11.4 0 0 0 3.6.6 1 1 0 0 1 1 1V20a1 1 0 0 1-1 1A17 17 0 0 1 3 4a1 1 0 0 1 1-1h3.5a1 1 0 0 1 1 1c0 1.25.2 2.45.6 3.6a1 1 0 0 1-.25 1z" fill="#fff"/></svg>
        <div><small>CALL US</small><b>(01) 555 0142</b></div>
      </div>
      <div class="item" style="left:270px">
        <svg width="16" height="16" viewBox="0 0 24 24"><circle cx="12" cy="12" r="9" fill="none" stroke="#fff" stroke-width="2"/><path d="M12 7v5l3 2" stroke="#fff" stroke-width="2" fill="none"/></svg>
        <div><small style="font-size:11px">OPENING HOURS</small><small>Mon - Sat: 8 am to 5 pm</small></div>
      </div>
      <div class="new-patients">NEW PATIENTS<small>Book An Appointment</small></div>
    </div>
  </header>

  <section>
    <h1 class="abs hero-title">THE TOOTH CORNER OF BRIMWELL</h1>
    <p class="abs hero-sub">Established Fact That A Reader Will Be Distracted By The Readable Content.</p>
    <a class="abs btn hero-btn">LEARN MORE</a>
  </section>

  <section>
    <h2 class="abs heading" style="top:822px">OUR SERVICES</h2>
    <div class="abs rule" style="top:883px"></div>
    <p class="abs services-intro">It is a long established fact that a reader will be distracted by the readable content of a page when looking at its layout. The point of using Lorem Ipsum is that it has a more-or-less normal distribution of letters.</p>

    <div class="abs service" style="left:91px;top:994px">
      <div class="ring"><div><svg width="70" height="70" viewBox="0 0 64 64" fill="none" stroke="#8dc63f" stroke-width="2.5"><path d="M14 12c6-4 10 0 16 0s10-4 16 0c6 4 4 14 1 22-2 6-2 18-6 18-5 0-4-14-9-14s-4 14-9 14c-4 0-4-12-6-18-3-8-5-18 1-22z"/><path d="M48 4l2 5 5 2-5 2-2 5-2-5-5-2 5-2z"/><path d="M46 44h10M46 50h10M46 56h10"/></svg></div></div>
      <h3>TEETH WHITENING</h3>
      <p>When you suffer from a foot and/or ankle problem, the pain and discomfort can make it...</p>
      <a class="btn">LEARN MORE</a>
    </div>
    <div class="abs service" style="left:340px;top:994px">
      <div class="ring"><div><svg width="70" height="70" viewBox="0 0 64 64" fill="none" stroke="#8dc63f" stroke-width="2.5"><path d="M14 14c6-4 10 0 18 0s12-4 18 0c6 4 4 14 1 22-2 6-3 20-7 20-5 0-5-16-12-16s-7 16-12 16c-4 0-5-14-7-20-3-8-5-18 1-22z"/><path d="M16 22h32M20 14v8M32 14v8M44 14v8"/></svg></div></div>
      <h3>DENTAL CROWNS</h3>
      <p>When you suffer from a foot and/or ankle problem, the pain and discomfort can make it...</p>
      <a class="btn">LEARN MORE</a>
    </div>
    <div class="abs service" style="left:592px;top:994px">
      <div class="ring"><div><svg width="70" height="70" viewBox="0 0 64 64" fill="none" stroke="#8dc63f" stroke-width="2.5"><path d="M14 10c6-4 10 0 18 0s12-4 18 0c6 4 4 14 1 22-2 6-3 22-7 22-5 0-5-16-12-16s-7 16-12 16c-4 0-5-16-7-22-3-8-5-18 1-22z"/><path d="M32 18v12M26 24h12"/></svg></div></div>
      <h3>PORCELAIN VENEERS</h3>
      <p>When you suffer from a foot and/or ankle problem, the pain and discomfort can make it...</p>
      <a class="btn">LEARN MORE</a>
    </div>
    <div class="abs service" style="left:856px;top:994px">
      <div class="ring"><div><svg width="70" height="70" viewBox="0 0 64 64" fill="none" stroke="#8dc63f" stroke-width="2.5"><rect x="8" y="14" width="48" height="36" rx="8"/><path d="M8 32h48M24 14v36M40 14v36"/><rect x="13" y="27" width="6" height="10"/><rect x="29" y="27" width="6" height="10"/><rect x="45" y="27" width="6" height="10"/></svg></div></div>
      <h3>ORTHODONTICS</h3>
      <p>When you suffer from a foot and/or ankle problem, the pain and discomfort can make it...</p>
      <a class="btn">LEARN MORE</a>
    </div>
  </section>

  <section>
    <h2 class="abs heading" style="top:1476px">ABOUT US</h2>
    <div class="abs rule" style="top:1537px"></div>
    <div class="abs doctor-photo" role="img" aria-label="Portrait of the dentist in a white coat"></div>
    <div class="abs doctor-name">Marisol Vega Ortiz</div>
    <p class="abs about-text">There are many variations of passages of Lorem Ipsum available, but the majority have suffered alteration in some form, by injected humour, or randomised words which don't look even slightly believable. If you are going to use a passage of Lorem Ipsum, you need to be sure there isn't anything embarrassing hidden in the middle of text. All the Lorem Ipsum generators on the Internet tend to repeat predefined chunks as necessary, making this the first true generator on the Internet. It uses a dictionary of over 200 Latin words, combined with a handful of model sentence structures, to generate Lorem Ipsum which looks reasonable.</p>
    <div class="abs circle-row" style="left:717px;top:1912px" aria-label="Social links"><span></span><span></span><span></span></div>
  </section>

  <section>
    <div class="abs testimonials"></div>
    <h2 class="abs heading" style="top:2213px">WHAT OUR PATIENTS SAY</h2>
    <div class="abs rule" style="top:2274px"></div>
    <svg class="abs" style="left:108px;top:2405px" width="26" height="50" viewBox="0 0 26 50"><path d="M24 2L3 25l21 23" fill="none" stroke="#999" stroke-width="2"/></svg>
    <svg class="abs" style="left:1066px;top:2405px" width="26" height="50" viewBox="0 0 26 50"><path d="M2 2l21 23L2 48" fill="none" stroke="#999" stroke-width="2"/></svg>
    <div class="abs avatar" role="img" aria-label="Patient portrait"></div>
    <div class="abs stars">★★★<span style="color:#e8b30e">★</span><span style="color:#ccc">☆</span></div>
    <p class="abs quote">There are many variations of passages of Lorem Ipsum available, but the majority have suffered alteration in some form, by injected humour, or randomised words which don't look even slightly believable. If you are going to use a passage of Lorem Ipsum, you need to be sure there isn't anything embarrassing.</p>
    <div class="abs patient">MR. PATIENT NAME<small>Patient</small></div>
  </section>

  <section>
    <svg class="abs contact-band" width="1200" height="700" viewBox="0 0 1200 700"><path d="M0 20 C140 0 260 60 360 120 C460 180 560 190 660 140 C760 90 820 40 940 60 C1060 80 1120 150 1200 160 L1200 700 L0 700 Z" fill="#0d55a5"/></svg>
    <div class="abs subscribe"><div class="field">Enter Your Email:</div><a class="btn">SUBSCRIBE</a></div>
    <h2 class="abs contact-title">CONTACT US</h2>
    <div class="abs contact-line" style="top:3015px">
      <svg width="20" height="24" viewBox="0 0 20 24"><path d="M10 0a8 8 0 0 0-8 8c0 6 8 16 8 16s8-10 8-16a8 8 0 0 0-8-8zm0 11a3 3 0 1 1 0-6 3 3 0 0 1 0 6z" fill="#fff"/></svg>
      <span>48 Harbor Lane, #12 Brimwell,<br>FL 30000</span>
    </div>
    <div class="abs contact-line" style="top:3068px;align-items:center">
      <svg width="24" height="24" viewBox="0 0 24 24"><circle cx="12" cy="12" r="11" fill="none" stroke="#fff" stroke-width="1.5"/><path d="M8.5 10.5a8 8 0 0 0 5 5l1.5-1.5 2.5 1v2.5c-5 .5-11-5.5-10.5-10.5H9.5l1 2.5z" fill="#fff"/></svg>
      <span>Call Us: <b>(01) 555 0142</b></span>
    </div>

    <div class="abs map" role="img" aria-label="Street map showing the clinic location"></div>

    <div class="abs appointment map-card">
      <h2>REQUEST AN APPOINTMENT</h2>
      <p>Passages of Lorem Ipsum available, but the majority</p>
      <div class="form">
        <div class="row"><div class="input">Name:</div><div class="input">Email:</div></div>
        <div class="row"><div class="input">Contact:</div><div class="input">Subject:</div></div>
        <div class="area">Contact:</div>
        <div class="submit">SUBMIT</div>
      </div>
    </div>
  </section>

  <footer class="abs footer">
    <div class="circle-row" aria-label="Social links"><span></span><span></span><span></span></div>
    <p class="copyright">©2018 THE TOOTH CORNER OF BRIMWELL, All Rights Reserved.</p>
  </footer>
</div>
</body>
</html>
```